Flyer für Wahlkampf
Zielgruppe
Ich benötige den Flyer für den Wahlkampf. Ich bin Kandidat für die Kommunalwahlen (Gemeinderats- und Kreistagswahl).
Aufgabenstellung
Der Flyer soll das Format DIN A5 haben und vier Seiten umfassen. Er soll einmal in der Mitte faltbar sein. Ob der Flyer in Hoch- oder Querformat erstellt wird, überlasse ich der Kreativität der Designer.
Die erste Seite soll das im Anhang beigefügte Bild von mir enthalten sowie die Angaben im beigefügten Word-Dokument. Idealerweise soll das Bild die ganze Seite einnehmen und die Angaben erscheinen an der Seite auf dem Bild. Ich überlasse dies jedoch der Kreativität der Designer.
Auf der zweiten Seite sollen die im Anhang beigefügten restlichen Bilder unter der Ruprik 'Meine bisherigen Erfolge für unsere Ortschaft:' erscheinen.
Der restliche Flyer soll dann nur aus Text bestehen, welcher kreativ angeordnet werden kann.
Allgemein habe ich hinsichtlich der Schriftart keine Vorstellungen und überlasse dies der Kreativität der Designer.
Dankeschön! :-)

```html
<!DOCTYPE html>
<html lang="de">
<head>
<meta charset="utf-8">
<title>Wahlkampf-Flyer – Innenseiten</title>
<link rel="stylesheet" href="https://fonts.googleapis.com/css2?family=Oswald:wght@500;700&family=Open+Sans:wght@400;700&display=swap">
<style>
  :root {
    --yellow: #f6c21c;
    --black: #1e1e1e;
    --ink: #2a2a2a;
    --paper: #ffffff;
    --shade: #f1f1f1;
    --stage: #d9d9d9;
    --photo-a: #3a3f4a;
    --photo-b: #7a6a5c;
  }
  * { box-sizing: border-box; margin: 0; padding: 0; }
  html, body { width: 1200px; height: 840px; overflow: hidden; }
  body {
    background: var(--stage);
    font-family: "Open Sans", Arial, sans-serif;
    color: var(--ink);
    position: relative;
  }
  .spread {
    position: absolute; left: 60px; top: 38px;
    width: 1080px; height: 764px;
    display: flex;
    box-shadow: 0 10px 30px rgba(0,0,0,.25);
  }
  .page {
    position: relative; width: 540px; height: 764px;
    background: linear-gradient(160deg, var(--paper) 55%, var(--shade) 100%);
    overflow: hidden;
  }
  .page--left { border-right: 1px solid #e2e2e2; }

  /* bands */
  .band { position: absolute; left: 0; width: 100%; }
  .band--top-yellow { top: 0; height: 80px; background: var(--yellow); clip-path: polygon(0 0, 100% 0, 100% 15%, 0 100%); }
  .band--top-black { top: 0; height: 80px; background: var(--black); clip-path: polygon(0 0, 100% 0, 100% 30%, 0 100%); }
  .band--bottom-yellow { bottom: 0; height: 90px; background: var(--yellow); clip-path: polygon(0 100%, 100% 0, 100% 100%); }

  /* about */
  .portrait {
    position: absolute; left: 24px; top: 22px; width: 170px; height: 170px;
    background: linear-gradient(150deg, var(--photo-b), var(--photo-a));
  }
  .about-label {
    position: absolute; left: 24px; top: 176px; width: 170px;
    background: var(--yellow); color: var(--black);
    font-family: "Oswald", "Arial Narrow", sans-serif; font-weight: 700;
    font-size: 17px; padding: 3px 10px;
  }
  .about-text {
    position: absolute; left: 206px; top: 46px; width: 312px;
    font-size: 10.5px; line-height: 1.42; text-align: justify;
  }
  .about-text strong { font-weight: 700; }

  h2.section-title {
    font-family: "Oswald", "Arial Narrow", sans-serif; font-weight: 700;
    letter-spacing: .2px;
  }
  .achievements-title {
    position: absolute; left: 24px; top: 214px; width: 500px;
    font-size: 23px; color: var(--black);
  }
  .achievements {
    position: absolute; left: 24px; top: 262px; width: 492px;
    display: flex; gap: 26px;
  }
  .achievements__column { flex: 1; list-style: none; }
  .achievements li {
    display: flex; gap: 10px; align-items: flex-start;
    font-size: 12.5px; line-height: 1.35; margin-bottom: 11px;
  }
  .achievements svg { flex: 0 0 22px; }

  .goals-title {
    position: absolute; left: 0; top: 432px; width: 100%;
    background: var(--black); color: var(--yellow);
    font-size: 21px; padding: 6px 24px;
  }
  .goal {
    font-size: 12px; line-height: 1.5; text-align: justify;
  }
  .goal strong { font-weight: 700; }
  .page--left .goal { position: absolute; left: 24px; top: 486px; width: 492px; }

  .goal-list { position: absolute; left: 30px; top: 88px; width: 482px; }
  .goal-list .goal { font-size: 11.8px; line-height: 1.48; margin-bottom: 13px; }
</style>
</head>
<body>
<main class="spread">
  <section class="page page--left">
    <div class="band band--top-yellow"></div>
    <div class="portrait" role="img" aria-label="Porträtfoto des Kandidaten"></div>
    <div class="about-label">Zu meiner Person:</div>
    <p class="about-text">Ich bin <strong>27</strong> Jahre alt, Finanzbeamter und seit 1999 wohnhaft in Lindenhain. Hier bin ich bereits in die Kita und die damalige Grundschule gegangen. Später besuchte ich die KGS Am Lindenberg. <strong>Seit 04/2021:</strong> Sachbearbeiter im Finanzamt der Region. <strong>Seit 07/2019:</strong> Mitglied im Ortschaftsrat und engagiert in der Gemeindearbeit. <strong>Seit 12/2019:</strong> Mitglied des Heimatvereins und aktiv im Kulturausschuss. Zudem bin ich ehrenamtlich Mitglied im TSV Lindenhain.</p>

    <h2 class="section-title achievements-title">Meine bisherigen Erfolge für unsere Ortschaft:</h2>
    <div class="achievements">
      <ul class="achievements__column">
        <li><svg width="22" height="22" viewBox="0 0 22 22"><rect x="1.5" y="3.5" width="17" height="17" fill="none" stroke="var(--yellow)" stroke-width="2.5"/><path d="M5 11l4 4 11-12" fill="none" stroke="var(--yellow)" stroke-width="3"/></svg><span>Asphaltierung der Friedhofstraße sowie weitere durchgeführte Tiefbaumaßnahmen</span></li>
        <li><svg width="22" height="22" viewBox="0 0 22 22"><rect x="1.5" y="3.5" width="17" height="17" fill="none" stroke="var(--yellow)" stroke-width="2.5"/><path d="M5 11l4 4 11-12" fill="none" stroke="var(--yellow)" stroke-width="3"/></svg><span>Sanierung der Friedhofs-Trauerhalle</span></li>
        <li><svg width="22" height="22" viewBox="0 0 22 22"><rect x="1.5" y="3.5" width="17" height="17" fill="none" stroke="var(--yellow)" stroke-width="2.5"/><path d="M5 11l4 4 11-12" fill="none" stroke="var(--yellow)" stroke-width="3"/></svg><span>flächendeckende Aufstellung von Abfallbehältern</span></li>
      </ul>
      <ul class="achievements__column">
        <li><svg width="22" height="22" viewBox="0 0 22 22"><rect x="1.5" y="3.5" width="17" height="17" fill="none" stroke="var(--yellow)" stroke-width="2.5"/><path d="M5 11l4 4 11-12" fill="none" stroke="var(--yellow)" stroke-width="3"/></svg><span>Errichtung eines Ortschaftsbüros</span></li>
        <li><svg width="22" height="22" viewBox="0 0 22 22"><rect x="1.5" y="3.5" width="17" height="17" fill="none" stroke="var(--yellow)" stroke-width="2.5"/><path d="M5 11l4 4 11-12" fill="none" stroke="var(--yellow)" stroke-width="3"/></svg><span>Aufstellung neuer Schaukästen</span></li>
        <li><svg width="22" height="22" viewBox="0 0 22 22"><rect x="1.5" y="3.5" width="17" height="17" fill="none" stroke="var(--yellow)" stroke-width="2.5"/><path d="M5 11l4 4 11-12" fill="none" stroke="var(--yellow)" stroke-width="3"/></svg><span>Aufstellung neuer Sitzbänke</span></li>
        <li><svg width="22" height="22" viewBox="0 0 22 22"><rect x="1.5" y="3.5" width="17" height="17" fill="none" stroke="var(--yellow)" stroke-width="2.5"/><path d="M5 11l4 4 11-12" fill="none" stroke="var(--yellow)" stroke-width="3"/></svg><span>Anschaffung einer Tischtennisplatte für den Spielplatz</span></li>
      </ul>
    </div>

    <h2 class="section-title goals-title">Was ich gerne noch bewirken möchte:</h2>
    <p class="goal"><strong>Mehr Geld für Tiefbaumaßnahmen</strong> – In den letzten Jahren lag der finanzielle Fokus des Gemeinderates auf Investitionen in die sozialen Bereiche – was ich auch sehr begrüße. Dennoch befinden sich einige Straßen und vor allem viele Fußwege in unserer Ortschaft in keinem guten Zustand. Auch in Sachen Barrierefreiheit besteht erheblicher Nachholbedarf. Daher möchte ich mich dafür einsetzen, dass zukünftig mehr Geld für Tiefbaumaßnahmen im Haushalt zur Verfügung steht und dieses entsprechend der bereits aufgestellten Prioritätenliste auch eingesetzt wird.</p>
  </section>

  <section class="page page--right">
    <div class="band band--top-black"></div>
    <div class="goal-list">
      <p class="goal"><strong>Sanierung der Turnhalle</strong> – Unsere Sportvereine tragen einen bedeutenden Teil zum kulturellen Leben in unserer Ortschaft bei. Leider befindet sich die Lindenhainer Turnhalle mittlerweile in keinem ansehnlichen und teilweise sogar in einem sanierungsbedürftigen Zustand. Ich möchte mich daher weiterhin für Investitionen in unsere Sportstätte stark machen. Insbesondere die Akquirierung von geeigneten Fördermitteln muss weiter vorangetrieben werden.</p>
      <p class="goal"><strong>Schaffung einer kleinen Einkaufsgelegenheit</strong> – Ein Thema, das viele Einwohner bewegt, sind fehlende Einkaufsmöglichkeiten im Dorf. Die gesetzlichen Hürden für die Errichtung eines Supermarktes in unserer Ortschaft sind leider sehr hoch. Es gibt jedoch eine Menge alternative Konzepte für kleinere Einkaufsgelegenheiten, mit denen der Einwohnerschaft zumindest die Dinge des täglichen Grundbedarfes zur Verfügung gestellt werden könnten. Hierzu hatte ich zuletzt Gespräche mit Investoren, die Interesse bekundeten, unsere Ortschaft entsprechend zu versorgen. Aus diesem Grund möchte ich das Projekt gerne weiterverfolgen und vorantreiben.</p>
      <p class="goal"><strong>Errichtung eines neuen Spielplatzes</strong> – Schon zum Heimatfest 2019 kamen viele Einwohnerinnen und Einwohner auf mich zu und äußerten den Wunsch nach einem Spielplatz in der Ortsmitte. In den letzten Jahren habe ich hierfür mit der Gemeindeverwaltung entsprechende Konzepte entwickelt, welche bisher noch nicht umgesetzt werden konnten. In der neuen Legislaturperiode möchte ich passende Fördermittel und Zuschüsse beschaffen und das Projekt nunmehr endlich realisieren.</p>
      <p class="goal"><strong>Neue Rad- und Gehwege</strong> – Viele Einwohner wünschen sich die Errichtung von Rad- und Gehwegen in Richtung B 112 bzw. nach Oberstadt. Das Sicherheitsgefühl würde sich dadurch für viele Verkehrsteilnehmer erhöhen. Es ist wichtig, hinsichtlich dieses Themas nichts zu beschönigen: Ohne Fördermittel wird die Gemeinde aufgrund der erheblichen Kosten nie dazu in der Lage sein, derartige Projekte zu realisieren. Dies bedeutet jedoch nicht, dass man hiervon gänzlich Abstand nehmen muss. Mein Bestreben ist, gezielte Planungen voranzutreiben und dass Lindenhain eine höhere Priorisierung im Radverkehrskonzept des Landkreises erhält. Somit steigen auch die Chancen auf Fördermittel.</p>
    </div>
    <div class="band band--bottom-yellow"></div>
  </section>
</main>
</body>
</html>
```